NEW Website DESIGN for Glass & Solid Surfaces Company

Brand New website, contemporary, clean, visual (images), not busy. ATTACHED IS OUR LOG THAT YOU MUST USE.

The company is called Brightfold Panes & Worktops (BrightfoldPW)
www.brightfoldpw.com
The website should be www.brightfoldpnw.com
one page for glass one page for solid surfaces www.brightfoldpanesplashes.co.uk
www.brightfoldpanesworktops.co.uk

Target Market(s)

Hotels, Commercial projects, Small focus on residential

Industry/Entity Type

Construction

Number of Pages Required

5+ page

Font styles to use
Sans Serif

Requirements
Must have
• COLOURS AS PER OUR LOGO - WHITE/YELLOW/GREY - WHITE BACK GROUND
• CLEAR SIMPLE NAVIGATION - MODER CLEAN CUT - DESIGN FEEL
• LATEST NAVIGATION FOR IMAGES and text to include per project details
• WORK/PROJECT AREA - NEWS AREA - TEAM AREA/ABOUT US/CONTACT US
• NEW PAGEwww.brightfoldpanesplashes.co.uk - NEW PAGE www.brightfoldpanesworktops.co.uk
• PLEASE COPY THIS TYPE OF TEMPALTE
• https://www.velmarbuild.co.uk/project/grand-suites/
• MOBILE READY
• WORDPRESS
• MODERN IMAGES INCLUDING LUMERAX HALVERN AND GLASS PROJECTS
Nice to have
• NEW DESIGN MODER FRESH
• WEBSITES I LIKE THE TEMPLATE SHOULD BE LIKE THE WEBSITE BELOW
• https://www.velmarbuild.co.uk/
Should not have
• NOT Old fashion template, not busy NAVIGATION
• NO BLACK
• NO DARK GREYS
• NOT LOTS OF YELLOW
• RESDENTIAL IMAGES

```html
<!DOCTYPE html>
<html lang="en">
<head>
<meta charset="utf-8">
<title>Brightfold Panes &amp; Worktops</title>
<link rel="stylesheet" href="https://fonts.googleapis.com/css2?family=Playfair+Display:ital,wght@0,400;1,400&family=Montserrat:wght@400;500;600&display=swap">
<style>
:root{
  --white:#ffffff;
  --mist:#f3f4f5;
  --mist-dark:#e6e8ea;
  --ink:#2a2b2d;
  --text:#4a4c50;
  --muted:#8a8d92;
  --line:#d4d6d9;
  --yellow:#dcc531;
  --wood:#8a6a4a;
}
*{margin:0;padding:0;box-sizing:border-box}
html,body{width:1200px;height:4592px;overflow:hidden}
body{position:relative;background:var(--white);font-family:"Montserrat",sans-serif;color:var(--text)}
.abs{position:absolute}
.serif{font-family:"Playfair Display",serif;font-weight:400;color:var(--ink)}
.photo{position:absolute}
.label{font-size:11px;letter-spacing:3px;text-transform:uppercase;font-weight:600;color:var(--ink)}
.arrow-link{display:flex;align-items:center;gap:14px}
.arrow-link svg{width:22px;height:10px}

/* sidebar */
.sidebar{left:0;top:0;width:80px;height:4592px;background:var(--white);z-index:5}
.brand-vert{left:14px;top:20px;width:52px;display:flex;flex-direction:column;align-items:center;gap:10px}
.brand-dot{width:34px;height:34px;border-radius:50%;border:3px solid var(--yellow)}
.brand-vert span{writing-mode:vertical-rl;transform:rotate(180deg);font-size:9px;color:var(--ink);letter-spacing:1px}
.menu{left:28px;top:380px;width:24px}
.menu i{display:block;height:2px;background:var(--ink);margin-bottom:6px}
.follow{left:32px;top:620px;writing-mode:vertical-rl;transform:rotate(180deg);font-size:9px;letter-spacing:1px;color:var(--muted)}
.social-col{left:34px;top:680px;display:flex;flex-direction:column;gap:20px}
.social-col i{width:12px;height:12px;border-radius:50%;background:var(--ink)}

/* hero */
.hero{left:80px;top:0;width:1120px;height:845px;background:linear-gradient(160deg,#e9e6e0 0%,#b9aa92 40%,#6e5640 75%,#4a3a2c 100%)}
.hero-kicker{left:661px;top:500px;color:var(--yellow);font-size:11px;letter-spacing:3px}
.hero-title{left:661px;top:525px;font-size:56px;line-height:62px;color:var(--white)}
.hero-copy{left:661px;top:672px;width:470px;font-size:15px;line-height:24px;color:var(--white)}
.hero-btn{left:80px;top:785px;width:215px;height:60px;background:var(--white);padding:0 36px}

/* about */
.about-bg{left:80px;top:845px;width:1120px;height:665px;background:var(--mist)}
.about-label{left:120px;top:940px;font-size:11px;letter-spacing:3px;color:var(--muted)}
.about-title{left:120px;top:958px;font-size:46px}
.about-rule{left:640px;top:996px;width:110px;height:1px;background:var(--ink)}
.about-copy{left:120px;top:1055px;width:510px;font-size:14px;line-height:26px}
.about-more{left:120px;top:1192px}
.about-quote{left:120px;top:1255px;width:520px;font-family:"Playfair Display",serif;font-style:italic;font-size:28px;line-height:40px;color:var(--ink)}
.mail-box{left:120px;top:1455px;width:52px;height:52px;background:var(--ink);display:flex;align-items:center;justify-content:center}

/* headings */
.section-title{left:0;width:1200px;padding-left:80px;text-align:center;font-size:46px}

/* projects */
.project-card{left:103px;top:1810px;width:287px;height:280px;background:var(--white);padding:40px 38px;box-shadow:0 2px 20px rgba(0,0,0,.06);z-index:2}
.project-card h3{font-size:30px;line-height:38px;font-weight:500;color:var(--ink)}
.project-card p{margin-top:18px;font-size:13px;color:var(--muted)}
.project-card .arrow-link{margin-top:30px}
.pager{left:945px;top:2320px;display:flex;gap:40px}

/* news */
.news{top:2590px;height:545px}
.news-featured{background:linear-gradient(180deg,#e4e4e2 0%,#f6f6f5 55%,#ffffff 100%)}
.news-date{font-size:11px;color:var(--ink)}
.news-title{margin-top:18px;font-size:32px;line-height:40px;color:var(--ink)}
.news-copy{margin-top:26px;font-size:13px;line-height:24px}
.news-read{position:absolute;left:0;bottom:95px}
.news-btn{left:452px;top:3005px;width:373px;height:56px;background:var(--ink);display:flex;justify-content:center;color:var(--yellow)}
.news-btn .label{color:var(--yellow)}

/* gallery & contact */
.lower-bg{left:80px;top:3135px;width:1120px;height:1305px;background:var(--mist)}
.skyline{left:80px;top:4290px;width:1120px;height:150px;background:linear-gradient(180deg,rgba(255,255,255,0) 0%,rgba(255,255,255,.7) 100%)}
.contact-sub{left:80px;width:1120px;text-align:center;top:4000px;font-size:14px;color:var(--muted)}
.field{background:var(--white);font-size:11px;color:var(--muted);padding:14px 20px}
.submit{left:340px;top:4205px;width:595px;height:52px;background:var(--ink);display:flex;align-items:center;justify-content:center}
.submit .label{color:var(--yellow)}

/* footer */
.footer-brand{left:135px;top:4470px;width:90px;text-align:center;font-size:9px;color:var(--ink)}
.footer-brand i{display:block;margin:0 auto 8px;width:52px;height:52px;border-radius:50%;border:4px solid var(--yellow)}
.foot-item{font-size:13px;line-height:20px;color:var(--ink);display:flex;gap:14px;align-items:flex-start}
.foot-item svg{width:18px;height:18px;flex:none;margin-top:1px}
.foot-social{left:982px;top:4478px;display:flex;gap:8px}
.foot-social i{width:30px;height:30px;border:1px solid var(--line);border-radius:50%;display:block}
.copyright{left:1105px;top:4482px;width:80px;font-size:9px;line-height:14px;color:var(--muted)}
</style>
</head>
<body>

<aside class="abs sidebar">
  <div class="abs brand-vert"><i class="brand-dot"></i><span>Brightfold Panes &amp; Worktops</span></div>
  <div class="abs menu"><i></i><i></i><i></i></div>
  <div class="abs follow">Follow</div>
  <div class="abs social-col"><i></i><i></i><i></i><i></i></div>
</aside>

<section>
  <div class="photo hero" role="img" aria-label="Bright kitchen with marble island, wooden ceiling beams and bar stools"></div>
  <div class="abs hero-kicker">KITCHEN</div>
  <h1 class="abs serif hero-title" style="color:var(--white)">Glass Splashbacks<br>Designed By You</h1>
  <p class="abs hero-copy">We supply and fit any bespoke Lumerax and glass products to our clients' specification, shape, finish and colour.</p>
  <a class="abs hero-btn arrow-link label">View Project
    <svg viewBox="0 0 22 10"><path d="M0 5h20M16 1l4 4-4 4" stroke="#2a2b2d" fill="none" stroke-width="1.4"/></svg></a>
</section>

<section>
  <div class="abs about-bg"></div>
  <div class="abs about-label">ABOUT</div>
  <h2 class="abs serif about-title">Brightfold Panes</h2>
  <div class="abs about-rule"></div>
  <p class="abs about-copy">We supply and fit any bespoke Lumerax and glass products to our clients' specification, shape, finish and colour: you imagine it, and we will help make it a reality. Crisp, clean and modern, they are the ultimate complement to the contemporary home or business.</p>
  <a class="abs about-more arrow-link label">Explore More
    <svg viewBox="0 0 22 10"><path d="M0 5h20M16 1l4 4-4 4" stroke="#2a2b2d" fill="none" stroke-width="1.4"/></svg></a>
  <blockquote class="abs about-quote">“Manufactured in house we have a vast range of mirror frames to suit all styles from modern to contemporary.</blockquote>
  <div class="abs mail-box"><svg width="20" height="16" viewBox="0 0 20 16"><rect x="1" y="1" width="18" height="14" fill="none" stroke="#fff" stroke-width="1.6"/><path d="M1 2l9 7 9-7" fill="none" stroke="#fff" stroke-width="1.6"/></svg></div>
  <div class="photo" style="left:670px;top:937px;width:478px;height:643px;background:linear-gradient(170deg,#e8e6e2 0%,#bdb3a4 45%,#8a7862 80%,#a4a09a 100%)" role="img" aria-label="Modern kitchen with stainless ovens, mosaic splashback and granite worktop with plant"></div>
</section>

<h2 class="abs serif section-title" style="top:1665px">Project Area</h2>
<section>
  <div class="photo" style="left:735px;top:1775px;width:413px;height:465px;background:linear-gradient(180deg,#e9e3da 0%,#a98c6a 60%,#6e5238 100%)" role="img" aria-label="Open kitchen with dark wood cabinets and white farmhouse sink"></div>
  <div class="photo" style="left:80px;top:2090px;width:410px;height:335px;background:linear-gradient(160deg,#eef0f0 0%,#cfcac2 50%,#9a7552 100%)" role="img" aria-label="Bright living room with stone fireplace, white sofa and wood floor"></div>
  <div class="photo" style="left:397px;top:1870px;width:458px;height:495px;background:linear-gradient(170deg,#d9c9a8 0%,#c8b088 40%,#8e6e4a 100%);z-index:1" role="img" aria-label="Open plan lounge and dining area with cream sofas and large windows"></div>
  <div class="abs project-card">
    <h3>BESPOKE<br>LUMERAX</h3>
    <p>Halvern™ Lumerax® is becoming the worksurface...</p>
    <a class="arrow-link label" style="font-size:10px">View Project
      <svg viewBox="0 0 22 10"><path d="M0 5h20M16 1l4 4-4 4" stroke="#2a2b2d" fill="none" stroke-width="1.4"/></svg></a>
  </div>
  <div class="abs pager label" style="font-size:10px"><span>← &nbsp;Prev</span><span>Next &nbsp;→</span></div>
</section>

<h2 class="abs serif section-title" style="top:2490px">Latest News</h2>
<section>
  <article class="abs news" style="left:113px;width:312px">
    <div class="news-date">Aug 6, 2018 &nbsp;|&nbsp; BPW-Admin</div>
    <h3 class="news-title" style="font-family:'Montserrat',sans-serif;font-weight:400">Spotlight on … our virtual office!</h3>
    <p class="news-copy">We are proud to have a virtual office at the Kingsley Innovation Centre in the heart of Ashford. It is important for us to have a presence in this vital city and this particular centre is second to none. […]</p>
    <a class="news-read arrow-link label" style="font-size:10px">Read Article <svg viewBox="0 0 22 10"><path d="M0 5h20M16 1l4 4-4 4" stroke="#8a8d92" fill="none" stroke-width="1.4"/></svg></a>
  </article>
  <article class="abs news news-featured" style="left:452px;width:373px;padding:0 34px" role="group">
    <div style="height:80px"></div>
    <div class="news-date">AUG 9, 2018 &nbsp;|&nbsp; BPW-Admin</div>
    <h3 class="news-title" style="font-family:'Montserrat',sans-serif;font-weight:400">Bathroom glass splashbacks at Harbon Hotel</h3>
    <p class="news-copy">We've been busy here at Brightfold Panes Splashbacks! We've been doing some fun residential jobs for lovely clients – our glass splashbacks can […]</p>
  </article>
  <a class="abs news-btn arrow-link"><span class="label" style="font-size:10px">Read Article</span> <svg viewBox="0 0 22 10"><path d="M0 5h20M16 1l4 4-4 4" stroke="#ffffff" fill="none" stroke-width="1.4"/></svg></a>
  <article class="abs news" style="left:860px;width:290px">
    <div class="news-date">Aug 2, 2018 &nbsp;|&nbsp; BPW-Admin</div>
    <h3 class="news-title" style="font-family:'Montserrat',sans-serif;font-weight:400">Glass Worktops in record time!</h3>
    <p class="news-copy">On our Throwback Thursday posts, we like to remember some of the great work we've done over the years! Back in 2014, we did these absolutely gorgeous glass worktops at The Fine Carve Kitchen. […]</p>
    <a class="news-read arrow-link label" style="font-size:10px">Read Article <svg viewBox="0 0 22 10"><path d="M0 5h20M16 1l4 4-4 4" stroke="#8a8d92" fill="none" stroke-width="1.4"/></svg></a>
  </article>
</section>

<section>
  <div class="abs lower-bg"></div>
  <h2 class="abs serif section-title" style="top:3185px">Photot Galary</h2>
  <div class="photo" style="left:80px;top:3300px;width:188px;height:555px;background:linear-gradient(180deg,#eceae6 0%,#c9c3ba 55%,#6a4c36 100%)" role="img" aria-label="Bathroom vanity with white basin and dark wood cabinet"></div>
  <div class="photo" style="left:282px;top:3300px;width:715px;height:555px;background:linear-gradient(170deg,#f1ede6 0%,#cfa878 40%,#9a7450 75%,#5c4634 100%)" role="img" aria-label="Kitchen with light wood cabinets, island and bar stools"></div>
  <div class="photo" style="left:1010px;top:3300px;width:190px;height:555px;background:linear-gradient(180deg,#eceae6 0%,#c8b596 60%,#8a6c4e 100%)" role="img" aria-label="Living room with built-in shelving and armchair"></div>

  <h2 class="abs serif section-title" style="top:3935px;font-size:40px">Get In Touch</h2>
  <p class="abs contact-sub">Feel free to contact me about anything.</p>
  <div class="abs field" style="left:340px;top:4065px;width:290px;height:52px">Name</div>
  <div class="abs field" style="left:340px;top:4132px;width:290px;height:52px">Email</div>
  <div class="abs field" style="left:643px;top:4065px;width:292px;height:119px">Message</div>
  <a class="abs submit"><span class="label" style="font-size:11px">Submit Now</span></a>
  <div class="abs skyline" role="img" aria-label="Faint city skyline silhouette"></div>
</section>

<footer>
  <div class="abs footer-brand"><i></i>Brightfold Panes &amp; Worktops</div>
  <div class="abs foot-item" style="left:275px;top:4480px;width:300px">
    <svg viewBox="0 0 18 18"><rect x="2" y="4" width="14" height="11" fill="none" stroke="#2a2b2d" stroke-width="1.4"/><path d="M2 8h14M6 4V2M12 4V2" stroke="#2a2b2d" stroke-width="1.4"/></svg>
    <span>Kingsley Business Centre, Harlow Lane<br>Ashford, AB4 0ZX</span></div>
  <div class="abs foot-item" style="left:630px;top:4476px">
    <svg viewBox="0 0 18 18"><path d="M4 2l3 0 1 4-2 1c1 2 3 4 5 5l1-2 4 1v3c-7 0-12-5-12-12z" fill="none" stroke="#2a2b2d" stroke-width="1.3"/></svg>
    <span>+44 (0)1632 960 548</span></div>
  <div class="abs foot-item" style="left:630px;top:4510px">
    <svg viewBox="0 0 18 18"><rect x="2" y="4" width="14" height="10" fill="none" stroke="#2a2b2d" stroke-width="1.3"/><path d="M2 5l7 5 7-5" fill="none" stroke="#2a2b2d" stroke-width="1.3"/></svg>
    <span>sales@brightfoldpanesplashes.co.uk</span></div>
  <div class="abs foot-social"><i></i><i></i><i></i></div>
  <div class="abs copyright">© 2018 Brightfold Panes &amp; Worktops</div>
</footer>

</body>
</html>
```